Brenton Civil

We need a Standard Professional Company Letterhead, company standard document template, coversheet template for a civil construction company. We would like the designs to use the company colour red

I have attached existing templates that need to improve greatly but please use as a quide of general layout.

```html
<!DOCTYPE html>
<html lang="en">
<head>
<meta charset="utf-8">
<title>Brenton Civil Pty Ltd – Letterhead</title>
<link href="https://fonts.googleapis.com/css2?family=Open+Sans:wght@400;600&family=Roboto:wght@400;500&display=swap" rel="stylesheet">
<style>
  :root {
    --brand-red: #c8202f;
    --ink: #3a3a3a;
    --ink-soft: #555555;
    --paper: #ffffff;
    --backdrop: #e4e4e6;
    --signature-tone: #ececec;
  }
  * { box-sizing: border-box; margin: 0; padding: 0; }
  html, body {
    width: 1063px;
    height: 1200px;
    overflow: hidden;
    background: var(--backdrop);
  }
  .letterhead {
    position: absolute;
    left: 140px;
    top: 36px;
    width: 783px;
    height: 1128px;
    background: var(--paper);
    box-shadow: 0 2px 10px rgba(0,0,0,0.12);
    font-family: "Open Sans", Arial, sans-serif;
    color: var(--ink-soft);
  }
  .contact-block {
    position: absolute;
    right: 92px;
    top: 70px;
    font-family: "Roboto", Arial, sans-serif;
    font-size: 14px;
    line-height: 18px;
    color: var(--ink);
  }
  .contact-line { display: flex; align-items: center; gap: 6px; }
  .contact-line.indented { padding-left: 10px; }
  .contact-icon { width: 12px; height: 12px; flex: none; }
  .brand {
    position: absolute;
    left: 70px;
    top: 160px;
    display: flex;
    align-items: center;
    gap: 14px;
  }
  .brand-dot {
    width: 70px;
    height: 70px;
    border-radius: 50%;
    background: var(--brand-red);
  }
  .brand-name {
    font-family: "Open Sans", Arial, sans-serif;
    font-weight: 600;
    font-size: 21px;
    line-height: 24px;
    color: var(--brand-red);
    text-transform: uppercase;
    letter-spacing: 0.5px;
  }
  .letter-body {
    position: absolute;
    left: 110px;
    top: 300px;
    width: 575px;
    font-size: 14.5px;
    line-height: 21px;
    letter-spacing: 0.3px;
  }
  .salutation { margin-bottom: 22px; }
  .letter-paragraph { margin-bottom: 22px; text-align: justify; text-align-last: left; }
  .closing { margin-top: 6px; }
  .signature-area {
    margin-top: 26px;
    margin-left: 20px;
    width: 110px;
    height: 70px;
    background: var(--signature-tone);
    border-radius: 4px;
  }
</style>
</head>
<body>
  <main class="letterhead">
    <header>
      <address class="contact-block" style="font-style: normal;">
        <div class="contact-line">PO Box 52 , Dunmore Qld 4799</div>
        <div class="contact-line indented">ABN : 12 345 678 901</div>
        <div class="contact-line indented">
          <svg class="contact-icon" viewBox="0 0 12 12" aria-hidden="true"><rect x="3" y="0.5" width="6" height="11" rx="1.2" fill="none" stroke="var(--brand-red)" stroke-width="1.3"/><circle cx="6" cy="9.6" r="0.7" fill="var(--brand-red)"/></svg>
          0400123456
        </div>
        <div class="contact-line indented">
          <svg class="contact-icon" viewBox="0 0 12 12" aria-hidden="true"><rect x="0.5" y="2.5" width="11" height="7.5" fill="var(--brand-red)"/><path d="M0.8 2.8 L6 7 L11.2 2.8" fill="none" stroke="#fff" stroke-width="1"/></svg>
          dan@brentoncivil.com.au
        </div>
        <div class="contact-line indented">
          <svg class="contact-icon" viewBox="0 0 12 12" aria-hidden="true"><circle cx="6" cy="6" r="5.5" fill="var(--brand-red)"/><path d="M0.5 6 H11.5 M6 0.5 C3 3.5 3 8.5 6 11.5 M6 0.5 C9 3.5 9 8.5 6 11.5" fill="none" stroke="#fff" stroke-width="0.8"/></svg>
          www.brentoncivil.com.au
        </div>
      </address>
      <div class="brand">
        <div class="brand-dot"></div>
        <div class="brand-name">Brenton Civil<br>Pty Ltd</div>
      </div>
    </header>

    <section class="letter-body">
      <p class="salutation">Dear customer,</p>
      <p class="letter-paragraph">Lorem ipsum dolor sit amet, consectetur adipisicing elit, sed do eiusmod tempor incididunt ut labore et dolore magna aliqua. Ut enim ad minim veniam, quis nostrud exercitation ullamco laboris nisi ut aliquip ex ea commodo consequat. Duis aute irure dolor in reprehenderit in voluptate velit esse cillum dolore eu fugiat nulla pariatur. Excepteur sint occaecat cupidatat non proident, sunt in culpa qui officia deserunt mollit anim id est laborum.</p>
      <p class="letter-paragraph">Lorem ipsum dolor sit amet, consectetur adipisicing elit, sed do eiusmod tempor incididunt ut labore et dolore magna aliqua. Ut enim ad minim veniam, quis nostrud exercitation ullamco laboris nisi ut aliquip ex ea commodo consequat. Duis aute irure dolor in reprehenderit in voluptate velit esse cillum dolore eu fugiat nulla pariatur. Excepteur sint occaecat cupidatat non proident, sunt in culpa qui officia deserunt mollit anim id est laborum.</p>
      <p class="letter-paragraph">Lorem ipsum dolor sit amet, consectetur adipisicing elit, sed do eiusmod tempor incididunt ut labore et dolore magna aliqua. Ut enim ad minim veniam, quis nostrud exercitation ullamco laboris nisi ut aliquip ex ea commodo consequat. Duis aute irure dolor in reprehenderit in voluptate velit esse cillum dolore eu fugiat nulla pariatur. Excepteur sint occaecat cupidatat non proident, sunt in culpa qui officia deserunt mollit anim id est laborum.</p>
      <p class="letter-paragraph">Lorem ipsum dolor sit amet, consectetur adipisicing elit, sed do eiusmod tempor incididunt ut labore et dolore magna aliqua. Ut enim ad minim veniam, quis nostrud exercitation ullamco laboris nisi ut aliquip ex ea commodo consequat. Duis aute irure dolor in reprehenderit.</p>
      <p class="closing">Yours Sincerely,</p>
      <div class="signature-area" role="img" aria-label="Handwritten signature"></div>
    </section>
  </main>
</body>
</html>
```